店舗オープン告知のはがき作成(裏面)をお願いいたします。
使用用途は、顧客様への配布と、他業種店舗様の店頭配置です。

○目を引いて、オープンすることが分かりやすいこと
○はがきの特典を感じていただき、オープンイベントに行こう!と思っていただけること

この2点を特に重視いたします。

静かさや穏やかさより、少し華やかな雰囲気がいいと思っております。

よろしくお願いいたします。

```html
<!DOCTYPE html>
<html lang="ja">
<head>
<meta charset="utf-8">
<title>ステラグレース オープンのご案内</title>
<link href="https://fonts.googleapis.com/css2?family=Noto+Serif+JP:wght@400;600;700;900&family=Noto+Sans+JP:wght@400;500;700&family=Cormorant+Garamond:wght@600;700&display=swap" rel="stylesheet">
<style>
:root{
  --green:#3f7d2a;
  --green-dark:#17391a;
  --green-deep:#0f2a12;
  --leaf:#8cbf5a;
  --pink:#e2578a;
  --gold:#d8b85a;
  --ink:#3a3a32;
  --white:#ffffff;
}
*{margin:0;padding:0;box-sizing:border-box}
html,body{width:837px;height:1200px;overflow:hidden;background:var(--white)}
body{font-family:"Noto Sans JP",sans-serif;color:var(--ink)}
.card{position:relative;width:837px;height:1200px;overflow:hidden;
  background:linear-gradient(180deg,#fbfdf6 0%,#f1f7e6 45%,#eef5e2 100%)}
.photo{position:absolute}
.photo-therapy{left:430px;top:140px;width:407px;height:300px;
  background:radial-gradient(ellipse at 60% 45%,#f7e6d8 0%,#eef1dd 45%,#cfe2b4 100%)}
.photo-flowers{left:0;top:220px;width:270px;height:360px;
  background:linear-gradient(160deg,#dfeccd 0%,#b9d59a 45%,#c9b7d9 100%)}
.photo-stones{left:630px;top:440px;width:207px;height:130px;
  background:linear-gradient(200deg,#f3e4ea 0%,#e4d6e6 50%,#d5e6c6 100%)}
.head{position:absolute;left:30px;top:22px}
.head .kicker{font-family:"Noto Serif JP",serif;font-weight:700;font-size:30px;color:var(--green)}
.head .brand{font-family:"Noto Serif JP",serif;font-weight:700;font-size:58px;color:var(--green);line-height:1.15;display:flex;align-items:center;gap:12px}
.head .brand i{display:block;width:16px;height:16px;border-radius:50%;background:var(--gold)}
.head .kana{font-family:"Noto Serif JP",serif;font-size:15px;color:var(--green);margin-left:250px;margin-top:-4px}
.tagline{position:absolute;left:30px;top:148px;font-family:"Noto Serif JP",serif;font-weight:600;font-size:22px;color:var(--green)}
.intro{position:absolute;left:30px;top:186px;font-size:13px;line-height:1.7;color:var(--ink)}
.sign{position:absolute;left:290px;top:236px;font-size:13px}
.open-badge{position:absolute;left:620px;top:30px;width:190px;text-align:center;
  font-family:"Cormorant Garamond",serif;color:var(--pink)}
.open-badge .date{font-size:74px;font-weight:700;line-height:1}
.open-badge .wed{display:inline-block;background:var(--pink);color:#fff;font-size:16px;padding:1px 10px;border-radius:10px;letter-spacing:.1em}
.open-badge .open{font-size:66px;font-weight:700;line-height:.95;color:var(--green);letter-spacing:.04em}
.services{position:absolute;left:290px;top:276px;width:340px}
.service{margin-bottom:12px}
.service h2{font-family:"Noto Serif JP",serif;font-weight:900;font-size:21px;color:var(--green);line-height:1.3}
.service p{font-size:13px;line-height:1.6;margin-top:4px;white-space:nowrap}
.event-band{position:absolute;left:0;top:584px;width:837px;height:46px;background:var(--green);
  color:#fff;font-family:"Noto Serif JP",serif;font-weight:900;font-size:25px;text-align:center;line-height:46px;letter-spacing:.04em}
.event-band::after{content:"";position:absolute;left:50%;bottom:-12px;margin-left:-14px;border:14px solid transparent;border-top:12px solid var(--green);border-bottom:0}
.perks{position:absolute;left:22px;top:650px;width:793px;display:flex;gap:14px}
.perk{position:relative;flex:1;height:280px;background:#fff;border:2px solid var(--leaf);border-radius:8px;overflow:hidden}
.perk .label{height:40px;background:var(--green);color:#fff;font-family:"Noto Serif JP",serif;font-weight:900;font-size:22px;text-align:right;padding-right:22px;line-height:40px}
.perk.special .label{background:var(--pink)}
.perk .days{position:absolute;left:8px;top:6px;width:72px;height:72px;border-radius:50%;background:var(--pink);border:3px solid #fff;
  color:#fff;font-family:"Cormorant Garamond",serif;font-weight:700;font-size:22px;line-height:1;display:flex;flex-direction:column;align-items:center;justify-content:center}
.perk .days small{font-size:14px}
.perk h3{font-family:"Noto Serif JP",serif;font-weight:900;font-size:22px;color:var(--green);text-align:center;margin-top:38px}
.perk p{font-size:12px;line-height:1.6;padding:4px 14px 0}
.perk .pic{position:absolute;left:12px;right:12px;bottom:12px;height:80px;border-radius:4px}
.pic-salt{background:linear-gradient(135deg,#e6dcf0,#c7b3df)}
.pic-hand{background:linear-gradient(135deg,#f5e7dc,#e3c7b6)}
.pic-crystal{background:linear-gradient(135deg,#fbe3ea,#f0bfcf)}
.perk.special h3{font-size:15px;color:var(--ink);font-weight:600;margin-top:36px}
.perk.special .gift{font-family:"Noto Serif JP",serif;font-weight:900;font-size:22px;color:var(--pink);text-align:center;line-height:1.35;margin-top:4px;padding:0}
.note{position:absolute;left:30px;top:940px;font-size:11px;color:var(--ink)}
.footer{position:absolute;left:0;top:966px;width:837px;height:234px;background:linear-gradient(180deg,var(--green-dark),var(--green-deep));color:#fff}
.footer .brand{position:absolute;left:30px;top:76px;font-family:"Noto Serif JP",serif;font-weight:700;font-size:32px;color:var(--gold);display:flex;align-items:center;gap:10px}
.footer .brand i{display:block;width:12px;height:12px;border-radius:50%;background:var(--gold)}
.footer .brand-kana{position:absolute;left:82px;top:124px;font-family:"Noto Serif JP",serif;font-size:13px;color:var(--gold)}
.contact{position:absolute;left:278px;top:42px}
.contact .addr{font-size:14px}
.contact .tel{font-family:"Noto Serif JP",serif;font-weight:900;font-size:30px;color:var(--gold);display:flex;align-items:center;gap:8px;margin-top:8px;white-space:nowrap}
.contact .hours{font-size:14px;margin-top:8px;line-height:1.6}
.map{position:absolute;right:20px;top:22px;width:150px;height:190px;background:linear-gradient(160deg,#f6f3e8,#e6e2d0);border-radius:4px}
</style>
</head>
<body>
<main class="card">
  <div class="photo photo-therapy" role="img" aria-label="アロマトリートメントを受けてくつろぐ女性の写真"></div>
  <div class="photo photo-flowers" role="img" aria-label="ラベンダーとハーブの花の写真"></div>
  <div class="photo photo-stones" role="img" aria-label="天然石アクセサリーの写真"></div>

  <header class="head">
    <p class="kicker">癒しサロン</p>
    <p class="brand"><i></i>Stella Grace</p>
    <p class="kana">ステラグレース</p>
  </header>
  <p class="tagline">〜穏やかな空間で心と体を休めていただきたい〜</p>
  <p class="intro">そんな思いでささやかなサロンを開業させていただくことになりました。<br>どうぞよろしくお願いいたします。</p>
  <p class="sign">代表　○○　○○</p>

  <div class="open-badge">
    <div class="date">8/1</div>
    <span class="wed">WED</span>
    <div class="open">OPEN</div>
  </div>

  <section class="services">
    <div class="service">
      <h2>アロマトリートメント・<br>スポーツアロマボディーケア</h2>
      <p>リラックスしたい方からスポーツ選手まで、<br>お体の状態に合わせた香りといやしでお身体をケアします。</p>
    </div>
    <div class="service">
      <h2>ハーブ販売</h2>
      <p>ハーバルセラピストがお客様の状態に合わせた<br>ハーブ選びをお手伝いいたします。</p>
    </div>
    <div class="service">
      <h2>天然石販売</h2>
      <p>手作りアクセサリーなど、さまざまな<br>天然石製品をご用意しております。<br>お好みのデザインでお作りいたします。</p>
    </div>
  </section>

  <h2 class="event-band">このハガキをご持参いただいた方への感謝イベント</h2>

  <section class="perks">
    <article class="perk">
      <div class="days">8/1<small>〜3</small></div>
      <div class="label">無料体験</div>
      <h3>バスソルト作り</h3>
      <p>アロマ精油とヒマラヤ岩塩で<br>バスソルトを作ってみましょう。</p>
      <div class="pic pic-salt" role="img" aria-label="手作りバスソルトの写真"></div>
    </article>
    <article class="perk">
      <div class="days">8/4<small>〜5</small></div>
      <div class="label">無料体験</div>
      <h3>ハンドトリートメント</h3>
      <p>天然植物オイルとアロマ精油で、<br>手のひらをやさしくほぐします。</p>
      <div class="pic pic-hand" role="img" aria-label="ハンドトリートメントの写真"></div>
    </article>
    <article class="perk special">
      <div class="days">8/1<small>〜5</small></div>
      <div class="label">特別企画</div>
      <h3>1,000円以上お買い上げの方に</h3>
      <p class="gift">かわいい水晶<br>プレゼント!</p>
      <div class="pic pic-crystal" role="img" aria-label="ピンクの水晶の写真"></div>
    </article>
  </section>

  <p class="note">※諸事情により内容が変更となる場合がございます。あらかじめご了承ください。</p>

  <footer class="footer">
    <p class="brand"><i></i>Stella Grace</p>
    <p class="brand-kana">ステラグレース</p>
    <div class="contact">
      <p class="addr">〒390-0000 長野県緑野市中町2丁目4-5</p>
      <p class="tel">
        <svg width="26" height="26" viewBox="0 0 24 24" aria-hidden="true"><path fill="#d8b85a" d="M6.6 10.8a15 15 0 0 0 6.6 6.6l2.2-2.2a1 1 0 0 1 1-.25 11.4 11.4 0 0 0 3.6.57 1 1 0 0 1 1 1V20a1 1 0 0 1-1 1A17 17 0 0 1 3 4a1 1 0 0 1 1-1h3.5a1 1 0 0 1 1 1c0 1.25.2 2.45.57 3.57a1 1 0 0 1-.25 1z"/></svg>
        TEL:0266-00-4821
      </p>
      <p class="hours">営業時間 11:00〜19:00(木曜日定休)<br>ご予約・お問い合わせはお気軽にどうぞ</p>
    </div>
    <div class="map" role="img" aria-label="サロン周辺の案内地図"></div>
  </footer>
</main>
</body>
</html>
```